New Book Cover Design Project for book about Selling Blend

DetWe need a book cover (front, back, spine) for a new book entitled ‘Selling Blend’’ and subtitled “Not Recipes But What Buyers Value” (inverted commas not to be part of the title and subtitle). The author is Malcolm Trevesby. The publisher is Lindenfold Press. The finished size of the paperback version will be 5" x 8" (127 x 203.2 mm). There will be paperback, hardback, and e-book versions. The final number of pages is expected to be in the region of 80 pages. Text for the back cover is in an attached document. At the bottom of the back cover should be publisher logo (rectangular) on the left and space for the ISBN bar code on the right. The design should be original and not include any stock images that have been created by someone else or may require obtaining a copyright licence to use. Symbols in common use and not copyrighted are probably ok. There are no required images, photographs or symbols except the publisher logo at the left bottom of the back cover. Spine lettering should be UK/US style with the top of the writing nearest the front cover. The designer is free to be creative using appropriate diagrams, symbols or abstract designs. A copy of the publisher logo is attached. Designers are assured that when evaluating designs absolutely no notice whatsoever is taken of a designer's Studio Hive ranking or status; We are completely output driven, so what matters is the design, not the ranking or status of the designer. In a similar way, designs are not evaluated as 'good' or 'bad' - the winning design will be chosen after review by a design review panel and is not decided arbitrarily by a single person. All submitted designs should be capable of effective copyright assignment. Designs submitted for consideration should include front cover, spine, and back cover.
Candidate Selling Blend words that can be included in designs, if the designer wishes, include: product, place, promotion, price, consumer, company objectives, participants, physical evidence, process of service assembly, battery life, usability, security, fashion, design, brand, appearance, health, obedience, sustainability, accessibility, value, idea, information operation, beliefs, vectors.

Target Market(s)

Academics, teachers, text book writers, and students concerned with marketing.

Industry/Entity Type

Education

Font styles to use
Serif

Requirements
Must have
• • Author on the front cover and the spine. Templates have been added to the brief for the cover with spine for a 80 page book. There are .indd and .pdf templates that can be used. the .indd and .pdf templates show where the ISBN blocks should go. The other .PDF templates have the ISBN in the wrong place (middle of the lower back cover) but have more information about the meanings of template markings. Bleeds - PLEASE NOTE - the cover printing is not exact - there is minor variation when the printers print the covers. Therefore do not have solid blocks of colour that go to the edges of the spine or spine and cover pages with different blocks of colour - solid blocks of colour may go round the spine folds a little bit! See the templates - they indicate the areas for possible printing imprecision. The ISBN numbers in the template file names are what will be used - perfect is for the paperback and case is for the hardback.
Nice to have
• • It is not necessary to have the subtitle on the spine. The final book size may not be 80 pages, therefore the spine width may change, but not by much. • Use only standard fonts.
Should not have
• • Ideally, stock images should not be used as we cannot control other uses of images created by other sources, thus potentially damaging the book branding. I don't like solid black cover or spine backgrounds.

```html
<!DOCTYPE html>
<html lang="en">
<head>
<meta charset="utf-8">
<title>Selling Blend – Cover Spread</title>
<link rel="stylesheet" href="https://fonts.googleapis.com/css2?family=Anton&family=Carlito:wght@400;700&family=Poppins:wght@400;700&display=swap">
<style>
  :root {
    --page-bg: #ffffff;
    --cover-deep: #0a2a62;
    --cover-mid: #123f88;
    --cover-light: #1a4d9c;
    --ink-light: #ffffff;
    --isbn-box: #ffffff;
  }
  * { margin: 0; padding: 0; box-sizing: border-box; }
  html, body {
    width: 829px; height: 1200px; overflow: hidden;
    background: var(--page-bg);
  }
  .spread {
    position: absolute; left: 16px; top: 285px;
    width: 797px; height: 630px;
    background: linear-gradient(160deg, var(--cover-deep) 0%, var(--cover-mid) 45%, var(--cover-light) 75%, var(--cover-mid) 100%);
    color: var(--ink-light);
    overflow: hidden;
  }
  .spread__texture {
    position: absolute; inset: 0;
    background: radial-gradient(ellipse at 75% 70%, rgba(40,100,190,0.35), transparent 60%),
                radial-gradient(ellipse at 30% 85%, rgba(8,30,80,0.35), transparent 55%);
  }
  .back { position: absolute; left: 0; top: 0; width: 397px; height: 630px; }
  .back__title {
    position: absolute; left: 0; width: 404px; top: 45px;
    text-align: center;
    font-family: "Anton", sans-serif; font-weight: 400; font-size: 32px; letter-spacing: 0.5px;
    line-height: 1;
  }
  .back__subtitle {
    position: absolute; left: 0; width: 404px; top: 84px;
    text-align: center;
    font-family: "Poppins", sans-serif; font-size: 14.5px; font-weight: 400;
  }
  .back__blurb {
    position: absolute; left: 38px; top: 107px; width: 327px;
    font-family: "Carlito", sans-serif; font-size: 11.2px; line-height: 14.9px;
    text-align: justify; text-align-last: center;
  }
  .back__about-heading {
    position: absolute; left: 38px; top: 402px;
    font-family: "Carlito", sans-serif; font-weight: 700; font-size: 11.4px;
  }
  .back__about-text {
    position: absolute; left: 38px; top: 417px; width: 322px;
    font-family: "Carlito", sans-serif; font-size: 11.2px; line-height: 14.9px;
  }
  .publisher-name {
    position: absolute; left: 38px; top: 548px;
    font-family: "Poppins", sans-serif; font-size: 16px; font-weight: 400;
    color: var(--ink-light);
  }
  .isbn-space {
    position: absolute; left: 218px; top: 510px; width: 153px; height: 92px;
    background: var(--isbn-box);
  }
  .spine-front { position: absolute; left: 0; top: 0; }
  .spine-front text { fill: var(--ink-light); }
  .spine-title, .spine-author { font-family: "Poppins", sans-serif; font-weight: 700; }
  .front-word { font-family: "Anton", sans-serif; }
  .front-subtitle { font-family: "Poppins", sans-serif; font-weight: 400; }
  .front-author { font-family: "Poppins", sans-serif; font-weight: 700; }
</style>
</head>
<body>
  <section class="spread">
    <div class="spread__texture" role="img" aria-label="Abstract network of connected points and faceted blue polygons across the cover"></div>

    <div class="back">
      <h1 class="back__title">SELLING BLEND</h1>
      <p class="back__subtitle">Not Recipes But What Buyers Value</p>
      <p class="back__blurb">Too many courses hand students a ready-made checklist for selling blend and ask them to fill in the boxes, rarely asking where that checklist came from or whether it still fits. This book argues that such shortcuts fall short of serious study. It traces a century of thinking on how offers reach people, and shows how much of that work has been quietly set aside. Rather than repeating a tidy formula, it asks readers to question it, to test it against real cases and to build their own view. Students are often told to draft a blend for a firm; the book explains why that task misses the point. It treats the blend as a tool for shaping ideas and beliefs as well as goods and services, and looks at how persuasion can work as a contest over information. It brings positioning into the centre of the discussion, and it follows the same logic into grey and unlawful trade, where the tools are used just as deliberately. Each argument is grounded in worked examples drawn from many settings.</p>
      <h2 class="back__about-heading">About the Author:</h2>
      <p class="back__about-text">Malcolm Trevesby has worked across business, universities and several charities focused on social justice. In each of these settings he has applied, taught and assessed selling practice, and that mix of roles shapes the challenging stance taken in this book.</p>
      <p class="publisher-name">Lindenfold Press</p>
      <div class="isbn-space"></div>
    </div>

    <svg class="spine-front" width="797" height="630" viewBox="0 0 797 630" xmlns="http://www.w3.org/2000/svg">
      <g class="spine">
        <text class="spine-title" font-size="12" transform="translate(393 46) rotate(90)" textLength="86" lengthAdjust="spacingAndGlyphs">SELLING BLEND</text>
        <text class="spine-author" font-size="12" transform="translate(393 461) rotate(90)" textLength="131" lengthAdjust="spacingAndGlyphs">MALCOLM TREVESBY</text>
      </g>
      <g class="front">
        <text class="front-word" font-size="108" transform="translate(506 540) rotate(-90)" textLength="499" lengthAdjust="spacingAndGlyphs">SELLING</text>
        <text class="front-word" x="515" y="164" font-size="168" textLength="249" lengthAdjust="spacingAndGlyphs">BLEND</text>
        <g class="front-subtitle" font-size="20.5" text-anchor="end">
          <text x="764" y="219">NOT</text>
          <text x="764" y="245">RECIPES</text>
          <text x="764" y="270">BUT</text>
          <text x="764" y="296">WHAT</text>
          <text x="764" y="322">BUYERS</text>
          <text x="764" y="347">VALUE</text>
        </g>
        <text class="front-author" x="428" y="590" font-size="34" textLength="337" lengthAdjust="spacingAndGlyphs">MALCOLM TREVESBY</text>
      </g>
    </svg>
  </section>
</body>
</html>
```